Real Estate Listing Signs for standard Yard arms

I need real estate listing signs done, for the standard sized sign to be hung beneath a white yard arm. To match existing logo. Information to be included:
-Logo
-Business name
-Phone number
-Marden Fosk Tundra Circle & Marden Fosk realty logos (smaller print)

Colors to be Red and anywhere in the gray scale between black and white, or a combination of those.

Target Market(s)

Drive by visuals

Industry/Entity Type

Real Estate Agent

Colors

Designer to choose only greyscale colors for use in the design.

Requirements
Must have
• My Logo and business name in same/similar font to whats provided, the MF tundra circle logo (small on bottom or corner somewhere), My phone number, and a decent amount of red coloration on the sign.

```html
<!DOCTYPE html>
<html lang="en">
<head>
<meta charset="utf-8">
<title>Valek Realty – Yard Sign</title>
<link href="https://fonts.googleapis.com/css2?family=Montserrat:wght@300;400;600;800;900&display=swap" rel="stylesheet">
<style>
  :root {
    --sign-red: #f5111f;
    --sign-black: #050505;
    --sign-white: #ffffff;
    --rule-grey: #9a9a9a;
    --canvas-bg: #e6e6e6;
  }
  * { margin: 0; padding: 0; box-sizing: border-box; }
  html, body { width: 1200px; height: 1200px; overflow: hidden; background: var(--canvas-bg); }
  body { font-family: "Montserrat", Arial, sans-serif; }

  .yard-sign {
    position: absolute;
    left: 160px; top: 40px;
    width: 880px; height: 1120px;
    background: var(--sign-black);
    overflow: hidden;
  }
  .sign-shapes { position: absolute; inset: 0; }

  .brand-block {
    position: absolute; left: 0; right: 0; top: 110px;
    display: flex; flex-direction: column; align-items: center;
    color: var(--sign-white);
  }
  .brand-mark {
    width: 110px; height: 110px;
    border: 14px solid var(--sign-white);
    margin-bottom: 44px;
  }
  .brand-name {
    font-weight: 900; font-size: 66px; line-height: 1.12;
    letter-spacing: 4px; text-align: center;
  }

  .agent-name {
    position: absolute; left: 0; right: 0; top: 560px;
    text-align: center; color: var(--sign-black);
  }
  .agent-first { font-weight: 300; font-size: 104px; line-height: 1; letter-spacing: 6px; }
  .agent-last { font-weight: 900; font-size: 124px; line-height: 1; letter-spacing: 2px; margin-top: 2px; }

  .contact-block {
    position: absolute; left: 0; right: 0; top: 835px;
    display: flex; flex-direction: column; align-items: center;
  }
  .phone-line { display: flex; align-items: center; gap: 22px; }
  .phone-icon { width: 62px; height: 62px; }
  .phone-number { color: var(--sign-red); font-weight: 800; font-size: 80px; line-height: 1; letter-spacing: 1px; }
  .email { color: var(--sign-white); font-weight: 300; font-size: 46px; letter-spacing: 3px; margin-top: 10px; }

  .broker-line {
    position: absolute; left: 70px; right: 70px; top: 1012px;
    display: flex; align-items: center; gap: 26px;
  }
  .broker-rule { flex: 1; height: 3px; background: var(--rule-grey); }
  .broker-name { color: var(--sign-white); text-align: center; line-height: 1.05; }
  .broker-group { font-weight: 600; font-size: 30px; letter-spacing: 1px; }
  .broker-realty { font-weight: 400; font-size: 14px; letter-spacing: 2px; }

  .disclaimer {
    position: absolute; left: 0; right: 0; top: 1078px;
    text-align: center; color: var(--sign-red);
    font-weight: 600; font-size: 19px; letter-spacing: 2px;
  }
</style>
</head>
<body>
  <main class="yard-sign">
    <svg class="sign-shapes" width="880" height="1120" viewBox="0 0 880 1120" aria-hidden="true">
      <rect x="36" y="36" width="808" height="560" fill="var(--sign-red)"/>
      <polygon points="0,430 880,590 880,800 0,800" fill="var(--sign-white)"/>
      <polygon points="250,500 450,552 680,548 450,541" fill="var(--sign-red)"/>
    </svg>

    <section class="brand-block">
      <div class="brand-mark"></div>
      <div class="brand-name">VALEK<br>REALTY</div>
    </section>

    <section class="agent-name">
      <div class="agent-first">JORDAN</div>
      <div class="agent-last">VALEK</div>
    </section>

    <section class="contact-block">
      <div class="phone-line">
        <svg class="phone-icon" viewBox="0 0 64 64" aria-hidden="true">
          <path d="M14 6c3 0 8 10 8 12s-5 5-5 7c0 4 12 17 17 17 2 0 5-5 7-5s12 5 12 8c0 4-6 11-11 11C27 56 8 37 8 18 8 12 11 6 14 6z" fill="var(--sign-white)"/>
          <path d="M36 14a14 14 0 0 1 14 14M38 4a24 24 0 0 1 22 22" stroke="var(--sign-white)" stroke-width="4" fill="none" stroke-linecap="round"/>
        </svg>
        <span class="phone-number">907-555-0148</span>
      </div>
      <div class="email">jvalek@example.com</div>
    </section>

    <section class="broker-line">
      <span class="broker-rule"></span>
      <div class="broker-name">
        <div class="broker-group">MF TUNDRA CIRCLE</div>
        <div class="broker-realty">MARDEN FOSK REALTY</div>
      </div>
      <span class="broker-rule"></span>
    </section>

    <p class="disclaimer">EACH OFFICE INDEPENDENTLY OWNED AND OPERATED</p>
  </main>
</body>
</html>
```